Creative Brief
RoveKeel
Business cards, Stationery, Power Points
Professional
Martin Quaile
Managing Director
1187 W Dorvan
Chicago, IL
info@RoveKeel.com
www.RoveKeel.com
Please put Pagebook, Chirper and Vid-Stream, Talkly symbols on the card
Please add a Talkly line with Talkly username rovekeel
Eat.Travel.Experience

```html
<!DOCTYPE html>
<html lang="en">
<head>
<meta charset="utf-8">
<title>RoveKeel Stationery</title>
<link href="https://fonts.googleapis.com/css2?family=Open+Sans:wght@400;600;700&display=swap" rel="stylesheet">
<style>
  :root{
    --backdrop:#e6e6e4;
    --paper:#ffffff;
    --ink:#1f3e63;
    --text:#4a4a4a;
    --muted:#8a8a8a;
    --charcoal:#3a3a3f;
    --teal:#2d6b80;
    --wave-blue:#3f80b3;
    --mark:#e0782c;
    --rule:#c9c9c9;
    --cell:#d9d9d9;
  }
  *{margin:0;padding:0;box-sizing:border-box}
  html,body{width:1200px;height:715px;overflow:hidden}
  body{background:var(--backdrop);font-family:"Open Sans",Arial,sans-serif;color:var(--text);position:relative}
  .piece{position:absolute;background:var(--paper);overflow:hidden;box-shadow:0 1px 3px rgba(0,0,0,.18)}
  .wave{position:absolute;left:0;bottom:0;width:100%;display:block}

  .brand{display:flex;align-items:center;gap:5px}
  .brand-dot{border-radius:50%;background:var(--mark);flex:none}
  .brand-name{font-weight:700;color:var(--ink);line-height:1;letter-spacing:-.2px}
  .brand.on-dark .brand-name{color:#fff}
  .brand-tag{font-size:4.5px;color:var(--muted);letter-spacing:.4px;margin-top:2px}

  /* business cards */
  .card{top:24px;width:192px;height:108px}
  .card-contact{left:24px}
  .card-logo{left:240px}
  .card-dark{left:458px;background:var(--charcoal)}
  .card-teal{left:678px;background:var(--teal)}
  .card-tagline{left:896px}
  .card .brand{position:absolute}
  .card-contact .brand{left:12px;top:12px}
  .card-contact .brand-dot{width:16px;height:16px}
  .card-contact .brand-name{font-size:14px}
  .card-person{position:absolute;left:12px;top:44px}
  .person-name{font-size:8.5px;font-weight:700;color:var(--ink)}
  .person-role{font-size:5.5px;color:var(--muted)}
  .card-details{position:absolute;left:112px;top:34px;padding-left:8px;border-left:1px solid var(--rule);font-size:4.8px;line-height:6.6px}
  .card-centered .brand{left:50%;top:50%;transform:translate(-50%,-50%)}
  .card-centered .brand-dot{width:20px;height:20px}
  .card-centered .brand-name{font-size:17px}
  .card-tagline .brand{top:38%}
  .tagline-band{position:absolute;left:0;right:0;top:72px;border-top:1px solid var(--rule);padding-top:5px;text-align:center;font-size:6.5px;font-weight:600;color:var(--teal);letter-spacing:.6px}

  /* envelope front */
  .envelope-front{left:24px;top:166px;width:384px;height:172px}
  .envelope-front .brand{position:absolute;left:14px;top:14px}
  .envelope-front .brand-dot{width:20px;height:20px}
  .envelope-front .brand-name{font-size:18px}
  .return-address{position:absolute;left:40px;top:44px;font-size:5.5px;color:var(--text)}

  /* envelope back */
  .envelope-back{left:24px;top:360px;width:384px;height:334px}
  .envelope-back svg{position:absolute;inset:0}
  .flap-mark{position:absolute;left:50%;transform:translateX(-50%)}
  .flap-mark.brand-dot{width:26px;height:26px}

  /* letterhead & fax */
  .sheet{top:160px;width:372px;height:535px}
  .letterhead{left:426px}
  .fax{left:808px}
  .sheet .brand{position:absolute;left:22px;top:20px}
  .sheet .brand-dot{width:24px;height:24px}
  .sheet .brand-name{font-size:21px}
  .letter-body{position:absolute;left:30px;top:78px;width:312px;font-size:5.6px;line-height:8px}
  .letter-body p{margin-bottom:8px}
  .recipient{margin-bottom:12px}
  .signature{width:60px;height:16px;background:linear-gradient(90deg,#dfe6ee,#b9c8d8);margin:4px 0 4px}
  .sheet-footer{position:absolute;right:16px;bottom:8px;text-align:right;font-size:4.8px;line-height:6.4px;color:#fff}

  .fax-title{position:absolute;right:22px;top:28px;font-size:13px;font-weight:700;color:var(--charcoal);letter-spacing:1px}
  .fax-table{position:absolute;left:22px;top:66px;width:328px;border-collapse:collapse;font-size:5.4px}
  .fax-table td{border:1px solid var(--rule);height:15px;padding:0 4px}
  .fax-table .label{background:var(--cell);width:36px;font-weight:600;color:var(--charcoal)}
  .fax-options{position:absolute;left:22px;top:136px;display:flex;gap:18px;font-size:5px}
  .fax-options span::before{content:"";display:inline-block;width:5px;height:5px;border:1px solid var(--muted);margin-right:3px;vertical-align:-1px}
  .fax-comments{position:absolute;left:22px;top:156px;width:328px;font-size:5.4px;font-weight:600;color:var(--charcoal);border-bottom:1px solid var(--rule);padding-bottom:3px}
</style>
</head>
<body>

  <!-- business cards -->
  <section class="piece card card-contact">
    <div class="brand"><span class="brand-dot"></span><div><div class="brand-name">RoveKeel</div><div class="brand-tag">Eat.Travel.Experience</div></div></div>
    <div class="card-person">
      <div class="person-name">Martin Quaile</div>
      <div class="person-role">Managing Director</div>
    </div>
    <div class="card-details">
      1187 W Dorvan<br>Chicago, IL<br>T 773 555 0147<br>F 773 555 0148<br>info@RoveKeel.com<br>www.RoveKeel.com<br>Talkly: rovekeel
    </div>
    <svg class="wave" viewBox="0 0 192 24" height="24" preserveAspectRatio="none">
      <path d="M0 24 L0 18 C70 6 130 6 192 12 L192 24Z" fill="var(--charcoal)"/>
      <path d="M0 14 C70 1 130 2 192 8" stroke="var(--wave-blue)" stroke-width="2" fill="none"/>
    </svg>
  </section>

  <section class="piece card card-logo card-centered">
    <div class="brand"><span class="brand-dot"></span><span class="brand-name">RoveKeel</span></div>
  </section>

  <section class="piece card card-dark card-centered">
    <div class="brand on-dark"><span class="brand-dot"></span><span class="brand-name">RoveKeel</span></div>
  </section>

  <section class="piece card card-teal card-centered">
    <div class="brand on-dark"><span class="brand-dot"></span><span class="brand-name">RoveKeel</span></div>
  </section>

  <section class="piece card card-tagline card-centered">
    <div class="brand"><span class="brand-dot"></span><span class="brand-name">RoveKeel</span></div>
    <div class="tagline-band">Eat &nbsp;|&nbsp; Travel &nbsp;|&nbsp; Experience</div>
  </section>

  <!-- envelope front -->
  <section class="piece envelope-front">
    <div class="brand"><span class="brand-dot"></span><span class="brand-name">RoveKeel</span></div>
    <div class="return-address">1187 W Dorvan, Chicago, IL</div>
    <svg class="wave" viewBox="0 0 384 40" height="40" preserveAspectRatio="none">
      <path d="M0 40 L0 30 C140 8 260 8 384 20 L384 40Z" fill="var(--charcoal)"/>
      <path d="M0 24 C140 2 260 3 384 13" stroke="var(--wave-blue)" stroke-width="3" fill="none"/>
    </svg>
  </section>

  <!-- envelope back -->
  <section class="piece envelope-back">
    <svg viewBox="0 0 384 334" width="384" height="334" preserveAspectRatio="none">
      <path d="M0 0 L192 110 L384 0" stroke="var(--rule)" stroke-width="1" fill="none"/>
      <path d="M0 0 L0 210 C80 150 150 128 192 128 C234 128 304 150 384 210 L384 0 L192 110Z" fill="#f7f7f7"/>
      <path d="M0 334 L0 230 C90 170 150 150 192 150 C234 150 294 170 384 230 L384 334Z" fill="var(--teal)"/>
      <path d="M0 334 L0 250 C90 190 150 172 192 172 C234 172 294 190 384 250 L384 334Z" fill="var(--charcoal)"/>
    </svg>
    <span class="brand-dot flap-mark" style="top:60px"></span>
    <span class="brand-dot flap-mark" style="top:180px"></span>
    <span class="brand-dot flap-mark" style="top:280px"></span>
  </section>

  <!-- letterhead -->
  <section class="piece sheet letterhead">
    <div class="brand"><span class="brand-dot"></span><div><div class="brand-name">RoveKeel</div><div class="brand-tag">Eat.Travel.Experience</div></div></div>
    <div class="letter-body">
      <p class="recipient">Madeline Harte<br>1452 Lorne St<br>Evanston, Illinois</p>
      <p>Dear Sir or Madam,</p>
      <p>Thank you for choosing us for your next journey. We plan each trip around good food, easy travel and moments worth keeping, so every day feels well paced and every stop feels worth the visit.</p>
      <p>Our team books local tables, quiet rooms and short transfers, and we stay on call from the first flight to the last. You simply pack, arrive and enjoy the places we have found for you.</p>
      <p>Please review the enclosed plan and let us know of any changes to dates, meals or rooms. We will confirm every detail in writing within two working days of your reply.</p>
      <p>We look forward to travelling with you.</p>
      <p>Yours Sincerely,</p>
      <div class="signature" role="img" aria-label="Handwritten signature"></div>
      <p>Martin Quaile</p>
    </div>
    <svg class="wave" viewBox="0 0 372 70" height="70" preserveAspectRatio="none">
      <path d="M0 70 L0 50 C130 12 250 10 372 30 L372 70Z" fill="var(--charcoal)"/>
      <path d="M0 42 C130 4 250 2 372 22" stroke="var(--wave-blue)" stroke-width="3" fill="none"/>
    </svg>
    <div class="sheet-footer">1187 W Dorvan, Chicago, IL<br>T 773 555 0147<br>www.RoveKeel.com</div>
  </section>

  <!-- fax -->
  <section class="piece sheet fax">
    <div class="brand"><span class="brand-dot"></span><div><div class="brand-name">RoveKeel</div><div class="brand-tag">Eat.Travel.Experience</div></div></div>
    <div class="fax-title">FAX</div>
    <table class="fax-table">
      <tr><td class="label">To</td><td></td><td class="label">From</td><td></td></tr>
      <tr><td class="label">Fax</td><td></td><td class="label">Pages</td><td></td></tr>
      <tr><td class="label">Phone</td><td></td><td class="label">Date</td><td></td></tr>
      <tr><td class="label">Re</td><td></td><td class="label">CC</td><td></td></tr>
    </table>
    <div class="fax-options">
      <span>Urgent</span><span>For Review</span><span>Please Comment</span><span>Please Reply</span><span>Please Recycle</span>
    </div>
    <div class="fax-comments">Comments:</div>
    <svg class="wave" viewBox="0 0 372 70" height="70" preserveAspectRatio="none">
      <path d="M0 70 L0 50 C130 12 250 10 372 30 L372 70Z" fill="var(--charcoal)"/>
      <path d="M0 42 C130 4 250 2 372 22" stroke="var(--wave-blue)" stroke-width="3" fill="none"/>
    </svg>
    <div class="sheet-footer">1187 W Dorvan, Chicago, IL<br>T 773 555 0147<br>www.RoveKeel.com</div>
  </section>

</body>
</html>
```